Business card/ stationary design for a pressure washing company
Commercial and Residential
Business card/ stationary design for a pressure washing company - Cleaning
Creative Brief
Simple
Marcus Delgado
N/A
Brookrinse@mailbox-demo.com
www.brookrinse-demo.com
Open to the idea of single or double sided business cards
brookrinse brookrinse
I have gone through the submissions that I have received so far and indicated a couple from each designer that I like. If you could please take that and apply it into a full stationary demo as well as a vehicle magnet, I would love to see how the design ideas transfer into the various applications. Thanks, Marcus
Also, a vehicle magnet would be very useful. Thanks!

```html
<!DOCTYPE html>
<html lang="en">
<head>
<meta charset="UTF-8">
<title>Brookrinse Business Cards</title>
<link href="https://fonts.googleapis.com/css2?family=Roboto:wght@400;700;900&display=swap" rel="stylesheet">
<style>
  :root {
    --bg: #e6e8ec;
    --card: #ffffff;
    --brand-blue: #1f5fd6;
    --deep-blue: #14379e;
    --panel-blue: #2a6ee8;
    --text-white: #ffffff;
    --shadow: rgba(20, 30, 60, 0.22);
  }
  html, body {
    margin: 0;
    padding: 0;
    width: 1200px;
    height: 820px;
    overflow: hidden;
    background: var(--bg);
    font-family: "Roboto", Arial, sans-serif;
  }
  .canvas {
    position: relative;
    width: 1200px;
    height: 820px;
  }
  .card {
    position: absolute;
    width: 540px;
    height: 310px;
    background: var(--card);
    border-radius: 22px;
    box-shadow: 0 10px 28px var(--shadow);
    overflow: hidden;
  }
  .card-front { left: 120px; top: 90px; }
  .card-back  { left: 540px; top: 420px; }

  .brand {
    position: absolute;
    display: flex;
    align-items: center;
    gap: 10px;
    white-space: nowrap;
  }
  .brand-dot {
    width: 26px;
    height: 26px;
    border-radius: 50%;
    background: var(--brand-blue);
    flex: none;
  }
  .brand-name {
    font-weight: 900;
    font-size: 44px;
    letter-spacing: 1px;
    color: var(--brand-blue);
    text-transform: uppercase;
  }
  .card-front .brand { left: 50%; top: 50%; transform: translate(-50%, -50%); }
  .card-back .brand { left: 28px; top: 78px; }
  .card-back .brand-name { font-size: 27px; letter-spacing: 0.5px; }
  .card-back .brand-dot { width: 18px; height: 18px; }

  .panel {
    position: absolute;
    inset: 0;
    width: 100%;
    height: 100%;
  }
  .contact {
    position: absolute;
    right: 24px;
    top: 34px;
    text-align: right;
    color: var(--text-white);
    font-size: 13px;
    line-height: 1.5;
    white-space: nowrap;
  }
  .contact-name { font-size: 23px; font-weight: 700; line-height: 1.1; }
  .contact-role { font-size: 16px; margin-bottom: 20px; }
  .contact-address { margin-bottom: 12px; }
  .contact-line { display: flex; justify-content: flex-end; align-items: center; gap: 6px; }
  .contact-line svg { width: 11px; height: 11px; fill: var(--text-white); flex: none; }
</style>
</head>
<body>
<div class="canvas">

  <section class="card card-front">
    <div class="brand">
      <span class="brand-dot"></span>
      <span class="brand-name">brookrinse</span>
    </div>
  </section>

  <section class="card card-back">
    <svg class="panel" viewBox="0 0 540 310" preserveAspectRatio="none">
      <path d="M288 0 C 236 80, 318 150, 250 218 C 210 258, 160 288, 138 310 L540 310 L540 0 Z" fill="var(--deep-blue)"/>
      <path d="M302 0 C 250 80, 332 150, 264 218 C 224 258, 174 288, 152 310 L540 310 L540 0 Z" fill="var(--panel-blue)"/>
    </svg>
    <div class="brand">
      <span class="brand-dot"></span>
      <span class="brand-name">brookrinse</span>
    </div>
    <div class="contact">
      <div class="contact-name">Lena Marlowe</div>
      <div class="contact-role">Director General</div>
      <div class="contact-address">Unit # 14, Harbor Row,<br>NY 10482</div>
      <div class="contact-line">555.214.0387
        <svg viewBox="0 0 24 24"><path d="M6.6 10.8a15 15 0 0 0 6.6 6.6l2.2-2.2c.3-.3.7-.4 1-.2 1.1.4 2.3.6 3.6.6.6 0 1 .4 1 1V20c0 .6-.4 1-1 1C10.6 21 3 13.4 3 4c0-.6.4-1 1-1h3.5c.6 0 1 .4 1 1 0 1.3.2 2.5.6 3.6.1.3 0 .7-.2 1z"/></svg>
      </div>
      <div class="contact-line">555-318-4026
        <svg viewBox="0 0 24 24"><path d="M7 2h10a2 2 0 0 1 2 2v16a2 2 0 0 1-2 2H7a2 2 0 0 1-2-2V4a2 2 0 0 1 2-2zm0 3v13h10V5z"/></svg>
      </div>
      <div class="contact-line">Brookrinse@mailbox-demo.com
        <svg viewBox="0 0 24 24"><path d="M3 5h18v14H3zm2 2v.5l7 4.5 7-4.5V7z"/></svg>
      </div>
      <div class="contact-line">www.brookrinse-demo.com
        <svg viewBox="0 0 24 24"><path d="M12 2a10 10 0 1 0 0 20 10 10 0 0 0 0-20zm0 2a8 8 0 1 1 0 16 8 8 0 0 1 0-16z"/></svg>
      </div>
    </div>
  </section>

</div>
</body>
</html>
```